Xmas Greeting for Email for Corvala Systems

We would love to have a beautifully designed Xmas card that we can send to our clients .
The card will be used to thank our clients for their support during the year and to wish them a Merry Xmas and a Good New year (2020).

We would like a design that is simple and very elegant.

Target Market(s)

Our clients

Font styles to use
Script

Colors

Designer to choose colors to be used in the design.

Requirements
Must have
• 1. Our logo (see attached)
• 2. A message that thanks our clients for their support during the year.
• 3. the message "Merry Christmas & Happy New Year"
• 4. Design must be simple and elegant

```html
<!DOCTYPE html>
<html lang="en">
<head>
<meta charset="utf-8">
<title>Corvala Systems – Season's Greetings</title>
<link rel="stylesheet" href="https://fonts.googleapis.com/css2?family=Great+Vibes&family=Raleway:wght@400;500&display=swap">
<style>
  :root {
    --page-bg: #ffffff;
    --card-top: #eee0db;
    --card-bottom: #e2c2bb;
    --teal: #2f5f63;
    --crimson: #9b1b30;
    --scene-sky: #ecd3cb;
    --scene-hill: #d9a47c;
    --scene-tree: #2e6461;
    --scene-snow: #f2ece8;
  }
  * { box-sizing: border-box; margin: 0; padding: 0; }
  html, body {
    width: 1200px; height: 960px; overflow: hidden;
    background: var(--page-bg);
  }
  .greeting-card {
    position: absolute;
    left: 280px; top: 40px;
    width: 640px; height: 880px;
    background: linear-gradient(160deg, var(--card-top) 0%, var(--card-bottom) 100%);
    display: flex; flex-direction: column; align-items: center;
    overflow: hidden;
    font-family: "Raleway", sans-serif;
    color: var(--teal);
    text-align: center;
  }
  .greeting-merry {
    margin-top: 118px;
    font-size: 24px; font-weight: 400;
    letter-spacing: 0.24em;
  }
  .greeting-christmas {
    font-family: "Great Vibes", cursive;
    font-weight: 400;
    font-size: 142px; line-height: 1;
    color: var(--crimson);
    margin-top: 2px;
  }
  .greeting-newyear {
    margin-top: 18px;
    font-size: 27px; font-weight: 500;
    letter-spacing: 0.2em;
  }
  .thanks-message {
    margin-top: 44px;
    font-size: 18px; line-height: 1.75;
  }
  .brand {
    margin-top: 44px;
    display: flex; align-items: center; gap: 12px;
  }
  .brand-dot {
    width: 34px; height: 34px; border-radius: 50%;
    background: var(--crimson);
  }
  .brand-name {
    font-size: 19px; font-weight: 500;
    letter-spacing: 0.16em;
    color: var(--crimson);
  }
  .village-scene {
    position: absolute; left: 0; bottom: 0;
    width: 100%; height: 330px;
    background: linear-gradient(180deg, rgba(236,211,203,0) 0%, var(--scene-hill) 45%, var(--scene-tree) 75%, var(--scene-snow) 100%);
  }
</style>
</head>
<body>
  <main class="greeting-card">
    <p class="greeting-merry">MERRY</p>
    <h1 class="greeting-christmas">Christmas</h1>
    <p class="greeting-newyear">AND HAPPY NEW YEAR</p>
    <p class="thanks-message">Thank very much for your loyalty.<br>We are very honor to have customer like you.</p>
    <div class="brand">
      <span class="brand-dot"></span>
      <span class="brand-name">CORVALA SYSTEMS</span>
    </div>
    <div class="village-scene" role="img" aria-label="Illustrated snowy village with red houses, teal pine trees, bare white trees, rolling hills and a person walking in the snow"></div>
  </main>
</body>
</html>
```